Soap/cosmetic labels

Need labels that incorporate my brand , to fit onto rectangular and round labels readable down to two inches. Key ideas are luxury, nourishing, handmade, palm oil/paraben free, cruelty free, savon artisanal. One line will be called The Tender Cake by The Dune Wanderer with key words: fragrance free, all natural colorants. The other line is luxury oils, fragrance, indulgent and just The Dune Wanderer

Target Market(s)

Women mostly

Industry/Entity Type

cosmetics/soap

Colors
0094D4
00A9DD
6FCCEA
C7EBF8
E9F6FB

Requirements
Must have
• place for me to change fragrance and cosmetic type; gold goes on black labels; blue on white labels
Nice to have
• fit the brand

```html
<!DOCTYPE html>
<html lang="en">
<head>
<meta charset="utf-8">
<title>The Tender Cake by The Dune Wanderer – Soap Label</title>
<link rel="stylesheet" href="https://fonts.googleapis.com/css2?family=Josefin+Sans:wght@400;600&display=swap">
<style>
  :root {
    --blue-deep: #0094D4;
    --blue-bright: #00A9DD;
    --blue-soft: #6FCCEA;
    --blue-pale: #C7EBF8;
    --blue-mist: #E9F6FB;
    --ink: #2b2b2b;
    --paper: #fbfbfb;
    --backdrop: #e4e5e6;
  }
  * { box-sizing: border-box; margin: 0; padding: 0; }
  html, body {
    width: 1200px; height: 781px; overflow: hidden;
    background: var(--backdrop);
    font-family: "Josefin Sans", sans-serif;
    color: var(--ink);
  }
  .label {
    position: absolute; left: 210px; top: 20px;
    width: 780px; height: 741px;
    background: var(--paper);
    box-shadow: 0 2px 10px rgba(0,0,0,.08);
  }
  .top-note {
    position: absolute; top: 26px; left: 0; width: 100%;
    text-align: center; font-size: 9px; letter-spacing: 6px;
    line-height: 13px; color: #777;
  }
  .tagline-frame {
    position: absolute; top: 262px; left: 420px; width: 360px; height: 30px;
  }
  .tagline {
    position: absolute; top: 283px; left: 478px;
    font-size: 15px; letter-spacing: 7px; background: var(--paper);
    padding: 0 8px;
  }
  .brand {
    position: absolute; top: 320px; left: 90px;
    display: flex; align-items: center; gap: 26px;
  }
  .brand-mark {
    width: 150px; height: 150px; border-radius: 50%;
    background: var(--blue-bright);
  }
  .brand-name {
    font-weight: 600; font-size: 62px; line-height: 1;
    color: var(--blue-bright); letter-spacing: 1px;
  }
  .brand-name .small { display: block; font-size: 34px; margin-left: 6px; }
  .subline {
    position: absolute; top: 492px; width: 100%; text-align: center;
    font-size: 14px; letter-spacing: 8px; line-height: 22px;
  }
  .keywords {
    position: absolute; top: 560px; left: 80px; width: 660px;
    display: flex; justify-content: space-between; align-items: center;
    list-style: none; font-size: 19px; font-weight: 600; letter-spacing: 1px;
  }
  .keywords li { padding: 0 20px; border-left: 1.5px solid var(--ink); line-height: 44px; }
  .keywords li:first-child { border-left: none; padding-left: 0; }
  .badges {
    position: absolute; top: 628px; left: 0; width: 100%;
    display: flex; justify-content: center; gap: 50px;
  }
  .badge { width: 76px; height: 76px; }
  .specs {
    position: absolute; bottom: 28px; left: 60px; right: 60px;
    display: flex; justify-content: space-between; font-size: 15px;
  }
  .spec-key { color: var(--blue-bright); font-weight: 600; margin-right: 8px; }
</style>
</head>
<body>
  <main class="label">
    <p class="top-note">FRAGRANCE FREE<br>ALL NATURAL COLORANTS</p>

    <svg class="tagline-frame" viewBox="0 0 360 30" aria-hidden="true">
      <polyline points="2,30 2,4 360,4" fill="none" stroke="#2b2b2b" stroke-width="1.5"/>
      <line x1="2" y1="28" x2="40" y2="28" stroke="#2b2b2b" stroke-width="1.5"/>
      <line x1="310" y1="28" x2="360" y2="28" stroke="#2b2b2b" stroke-width="1.5"/>
    </svg>
    <p class="tagline">TENDER CAKE BY</p>

    <div class="brand">
      <div class="brand-mark"></div>
      <h1 class="brand-name"><span class="small">The</span>Dune Wanderer</h1>
    </div>

    <p class="subline">LUXURY OIL<br>ALL NATURAL COLORANTS</p>

    <ul class="keywords">
      <li>LUXURY</li>
      <li>NOURISHING</li>
      <li>HANDMADE</li>
      <li>PALM OIL</li>
    </ul>

    <div class="badges">
      <svg class="badge" viewBox="0 0 76 76" role="img" aria-label="Paraben free badge">
        <circle cx="38" cy="38" r="34" fill="none" stroke="#00A9DD" stroke-width="2"/>
      </svg>
      <svg class="badge" viewBox="0 0 76 76" role="img" aria-label="Cruelty free badge">
        <circle cx="38" cy="38" r="34" fill="none" stroke="#00A9DD" stroke-width="2"/>
      </svg>
    </div>

    <div class="specs">
      <p><span class="spec-key">FRAGRANCE :</span>LOREM IPSUM</p>
      <p><span class="spec-key">COSMETIC TYPE:</span>LOREM IPSUM</p>
    </div>
  </main>
</body>
</html>
```